Redesign of Engineering firm website

I want a redesign of the torvelpower.com website with the below in mind:

1- the client has a 3 main sectors: Renewable Energy, Process Automation and General Engineering.
2- Home page should show the 3 sectors
3- the other standard pages should be home, About, Clients, Projects, Training, Career, and Contact
4- The theme should be wordpress.
5- Responsive layout that works with all devices
6- One page layout is preferable for the home page.
7- it should be original and is not copied from other templates.
Updates

Reason: As requested from so many designers... the deadline is extended. Thank you

Target Market(s)

Engineers and professional

Industry/Entity Type

Solar Energy

Font styles to use
Serif
Sans Serif

Colors
3277b5
0355a3
0493ce

Requirements
Must have
• pictures that represent the three sectors

```html
<!DOCTYPE html>
<html lang="en">
<head>
<meta charset="utf-8">
<title>Torvel Power</title>
<link rel="stylesheet" href="https://fonts.googleapis.com/css2?family=Roboto:wght@300;400;500&family=Arimo:wght@400&family=Roboto+Slab:wght@400&display=swap">
<style>
:root{
  --brand:#0493ce;
  --brand-dark:#0355a3;
  --brand-mid:#3277b5;
  --ink:#2b2b2b;
  --text:#6b6b6b;
  --soft:#f4f5f7;
  --line:#dcdcdc;
  --white:#fff;
}
*{margin:0;padding:0;box-sizing:border-box}
html,body{width:690px;height:1200px;overflow:hidden;background:var(--white)}
body{position:relative;font-family:"Arimo",Arial,sans-serif;color:var(--text)}
.heading{font-family:"Roboto",Arial,sans-serif;color:var(--ink)}
.accent{color:var(--brand)}
section,header,footer{position:absolute;left:0;width:690px}

/* header */
.site-header{top:0;height:54px;background:var(--white);border-bottom:1px solid #eee}
.logo{position:absolute;font-family:"Roboto",Arial,sans-serif;font-weight:500;color:var(--brand-mid);letter-spacing:.5px}
.site-header .logo{left:50px;top:12px;font-size:23px}
.nav{position:absolute;left:0;top:24px;width:690px;height:10px;font-family:"Roboto",Arial,sans-serif;font-size:7px;font-weight:500;color:#555;letter-spacing:.1px}
.nav span{position:absolute;top:0;white-space:nowrap}
.nav .active{color:var(--brand)}
.search{position:absolute;left:611px;top:13px;width:29px;height:29px;border:1.5px solid var(--brand);border-radius:50%}
.search svg{position:absolute;left:8px;top:8px}

/* hero */
.hero{top:54px;height:288px}
.hero-photo{position:absolute;inset:0;background:linear-gradient(180deg,#5d9ed1 0%,#3f86c2 45%,#2c6aa3 70%,#1f4f80 100%)}
.hero-arrow{position:absolute;top:129px;width:30px;height:30px;border:1.5px solid var(--white);border-radius:50%}
.hero-arrow svg{position:absolute;left:9px;top:8px}
.hero-title{position:absolute;left:426px;top:84px;font-family:"Roboto",Arial,sans-serif;font-weight:300;font-size:22px;color:var(--white);letter-spacing:.5px}
.hero-text{position:absolute;left:426px;top:118px;width:210px;font-size:6.5px;line-height:14px;color:var(--white)}
.hero-btn{position:absolute;left:427px;top:173px;width:72px;height:24px;border:1px solid var(--white);color:var(--white);font-family:"Roboto",Arial,sans-serif;font-size:7.5px;text-align:center;line-height:22px}

/* sectors */
.sectors{top:342px;height:242px}
.sector{position:absolute;top:16px;width:190px}
.sector h3{font-size:10px;font-weight:500;letter-spacing:.2px;margin-bottom:11px}
.sector .photo{width:189px;height:121px;border:1px solid var(--line);padding:2px;background:var(--white)}
.sector .photo div{width:100%;height:100%}
.sector p{margin-top:13px;width:186px;font-size:6.4px;line-height:15px}

/* about + news */
.about-news{top:584px;height:202px;background:var(--soft)}
.about{position:absolute;left:50px;top:21px;width:350px}
.section-title{font-size:14px;font-weight:400}
.about p{font-size:6.3px;line-height:13.6px;margin-top:12px}
.about p+p{margin-top:12px}
.read-more{display:inline-block;margin-top:11px;font-family:"Roboto",Arial,sans-serif;font-size:7.5px;color:var(--brand-dark);text-decoration:underline;font-weight:500}
.news{position:absolute;left:424px;top:22px;width:220px}
.news-item{position:relative;margin-top:14px;height:64px}
.news-item+.news-item{margin-top:10px}
.news-date{position:absolute;left:0;top:0;width:32px;text-align:center;font-family:"Roboto Slab",Georgia,serif}
.news-date b{display:block;font-size:20px;font-weight:400;color:var(--brand);line-height:20px}
.news-date i{display:block;font-size:9px;font-style:normal;color:var(--ink);margin-top:2px}
.news-body{position:absolute;left:39px;top:0;width:185px}
.news-body h4{font-family:"Roboto",Arial,sans-serif;font-size:7px;font-weight:500;color:#333}
.news-body p{font-size:6.2px;line-height:14.4px;margin-top:5px}

/* training */
.training{top:786px;height:230px}
.training-copy{position:absolute;left:50px;top:25px;width:320px}
.training-copy p{font-size:6.3px;line-height:13.6px;margin-top:13px}
.course-list{list-style:none;margin-top:12px}
.course-list li{position:relative;padding-left:17px;font-size:6.3px;line-height:18.3px}
.course-list svg{position:absolute;left:0;top:5px}
.devices{position:absolute;left:404px;top:20px;width:232px;height:170px;border-radius:4px;background:linear-gradient(160deg,#eef1f4 0%,#c9d2da 100%)}

/* footer */
.site-footer{top:1016px;height:146px;background:var(--soft)}
.site-footer .logo{left:50px;top:56px;font-size:28px}
.foot-col{position:absolute;top:30px}
.foot-col h5{font-family:"Roboto",Arial,sans-serif;font-size:9px;font-weight:400;color:#444;letter-spacing:.2px}
.contact-list{list-style:none;margin-top:15px}
.contact-list li{position:relative;padding-left:15px;font-size:6.3px;line-height:16.5px;color:#555}
.contact-list svg{position:absolute;left:0;top:4px}
.contact-list .mail{color:var(--brand-dark);text-decoration:underline}
.foot-col p{font-size:6.3px;line-height:11.5px;margin-top:14px;color:#666}
.email-field{margin-top:9px;width:122px;height:19px;border:1px solid var(--line);background:var(--white);font-size:6.3px;line-height:17px;padding-left:8px;color:#666}
.subscribe{margin-top:9px;width:47px;height:16px;background:var(--brand-dark);color:var(--white);font-family:"Roboto",Arial,sans-serif;font-size:5.5px;font-weight:500;text-align:center;line-height:16px}
.social{display:flex;gap:5px;margin-top:13px}
.social span{width:20px;height:20px;border:1px solid #bdbdbd;border-radius:50%}
.copyright{position:absolute;left:0;width:690px;top:1162px;height:38px;background:var(--brand-dark);color:var(--white);font-size:6.8px;text-align:center;line-height:38px}
</style>
</head>
<body>

<header class="site-header">
  <div class="logo">TORVEL</div>
  <nav class="nav">
    <span class="active" style="left:246px">HOME</span>
    <span style="left:293px">ABOUT</span>
    <span style="left:342px">CLIENTS</span>
    <span style="left:397px">PROJECTS</span>
    <span style="left:459px">TRAINING</span>
    <span style="left:519px">CAREER</span>
    <span style="left:572px">CONTACT</span>
  </nav>
  <div class="search"><svg width="11" height="11" viewBox="0 0 11 11"><circle cx="4.5" cy="4.5" r="3" fill="none" stroke="#0493ce" stroke-width="1.4"/><line x1="6.8" y1="6.8" x2="9.5" y2="9.5" stroke="#0493ce" stroke-width="1.4"/></svg></div>
</header>

<section class="hero">
  <div class="hero-photo" role="img" aria-label="Offshore wind turbines standing in a row over the sea under a blue sky"></div>
  <div class="hero-arrow" style="left:14px"><svg width="10" height="12" viewBox="0 0 10 12"><polyline points="7,1 2,6 7,11" fill="none" stroke="#fff" stroke-width="2"/></svg></div>
  <div class="hero-arrow" style="left:645px"><svg width="10" height="12" viewBox="0 0 10 12"><polyline points="3,1 8,6 3,11" fill="none" stroke="#fff" stroke-width="2"/></svg></div>
  <h1 class="hero-title">TORVEL POWER</h1>
  <p class="hero-text">We provide our services, both by our in-house team &amp; associated partners. All together have diversified expertise covering various aspects of solar&nbsp; related aspects of solar PV.</p>
  <div class="hero-btn">READ MORE</div>
</section>

<section class="sectors">
  <article class="sector" style="left:50px">
    <h3 class="heading">RENEWABLE ENERGY</h3>
    <div class="photo"><div role="img" aria-label="Wind turbines on a green field" style="background:linear-gradient(180deg,#d9e6ee 0%,#b7cfc0 45%,#5f8d3c 70%,#3d6a2a 100%)"></div></div>
    <p>We are the solar experts in the solar kingdom. The KSA (Saudi Arabia) solar market is a promising market with huge solar in the coming 20 years, as announced</p>
  </article>
  <article class="sector" style="left:251px">
    <h3 class="heading">PROCESS AUTOMATION</h3>
    <div class="photo"><div role="img" aria-label="Hand touching a digital automation interface" style="background:linear-gradient(135deg,#1f3f6e 0%,#3a6aa6 55%,#5b95cf 100%)"></div></div>
    <p>We are the solar experts in the solar kingdom. The KSA (Saudi Arabia) solar market is a promising market with huge solar in the coming 20 years, as announced</p>
  </article>
  <article class="sector" style="left:451px">
    <h3 class="heading">GENERAL ENGINEERING</h3>
    <div class="photo"><div role="img" aria-label="Engineers reviewing drawings at a desk with a laptop" style="background:linear-gradient(135deg,#f1ede8 0%,#d8cbbd 55%,#a8835f 100%)"></div></div>
    <p>We are the solar experts in the solar kingdom. The KSA (Saudi Arabia) solar market is a promising market with huge solar in the coming 20 years, as announced</p>
  </article>
</section>

<section class="about-news">
  <div class="about">
    <h2 class="heading section-title">About <span class="accent">Torvel</span></h2>
    <p>We are the solar experts in the solar kingdom. The KSA (Saudi Arabia) solar market is a promising market with huge potential. The plan is to build 41,000 MW of solar in the coming 20 years, as announced by N.E.A (National Energy Agency). We provide our services, both by our in-house team and associated partners. All together have diversified expertise covering various aspects of solar PV.</p>
    <p>Our network of government officials, real estate experts, market analyst, and industry professionals track the market in real time, and turn knowledge to experience and value to our clients. real estate experts, market analyst,&nbsp; real time, and turn knowledge to experience and value to our clients.</p>
    <span class="read-more">Read More</span>
  </div>
  <div class="news">
    <h2 class="heading section-title">Our <span class="accent">News</span></h2>
    <div class="news-item">
      <div class="news-date"><b>09</b><i>FEB</i></div>
      <div class="news-body"><h4>We are the solar experts in the solar kingdom</h4><p>We provide our services, both by our in-house team and associated partners. All together have diversified expertise covering various aspects of solar PV.</p></div>
    </div>
    <div class="news-item">
      <div class="news-date"><b>09</b><i>FEB</i></div>
      <div class="news-body"><h4>We are the solar experts in the solar kingdom</h4><p>We provide our services, both by our in-house team and associated partners. All together have diversified expertise covering various aspects of solar PV.</p></div>
    </div>
  </div>
</section>

<section class="training">
  <div class="training-copy">
    <h2 class="heading section-title">Training <span class="accent">Courses</span></h2>
    <p>Torvel-Solar: provides Solar Energy consulting services, Energy Efficiency Consulting services and Data Collection function. With services spanning the entire project lifecycle, Torvel scope goes beyond engineering, procurement and construction</p>
    <ul class="course-list">
      <li><svg width="8" height="8" viewBox="0 0 8 8"><circle cx="4" cy="4" r="3.3" fill="none" stroke="#0493ce" stroke-width="1.2"/><polyline points="3.3,2.5 4.8,4 3.3,5.5" fill="none" stroke="#0493ce" stroke-width="1.1"/></svg>Provide Solar Energy consulting services</li>
      <li><svg width="8" height="8" viewBox="0 0 8 8"><circle cx="4" cy="4" r="3.3" fill="none" stroke="#0493ce" stroke-width="1.2"/><polyline points="3.3,2.5 4.8,4 3.3,5.5" fill="none" stroke="#0493ce" stroke-width="1.1"/></svg>Provide Energy Efficiency Consulting services</li>
      <li><svg width="8" height="8" viewBox="0 0 8 8"><circle cx="4" cy="4" r="3.3" fill="none" stroke="#0493ce" stroke-width="1.2"/><polyline points="3.3,2.5 4.8,4 3.3,5.5" fill="none" stroke="#0493ce" stroke-width="1.1"/></svg>Provide Representation Services</li>
      <li><svg width="8" height="8" viewBox="0 0 8 8"><circle cx="4" cy="4" r="3.3" fill="none" stroke="#0493ce" stroke-width="1.2"/><polyline points="3.3,2.5 4.8,4 3.3,5.5" fill="none" stroke="#0493ce" stroke-width="1.1"/></svg>Provide Sole Sales Agent-ship services for materials and help to establish manufacturing faculties.</li>
      <li><svg width="8" height="8" viewBox="0 0 8 8"><circle cx="4" cy="4" r="3.3" fill="none" stroke="#0493ce" stroke-width="1.2"/><polyline points="3.3,2.5 4.8,4 3.3,5.5" fill="none" stroke="#0493ce" stroke-width="1.1"/></svg>Become Data Collection and knowledge distribution agency</li>
    </ul>
  </div>
  <div class="devices" role="img" aria-label="Desktop monitor and tablet showing the company website"></div>
</section>

<footer class="site-footer">
  <div class="logo">TORVEL</div>
  <div class="foot-col" style="left:198px">
    <h5>CONTACT US</h5>
    <ul class="contact-list">
      <li><svg width="8" height="8" viewBox="0 0 8 8"><path d="M1 1h2l.6 1.6-1 .7a4 4 0 0 0 2.1 2.1l.7-1L7 5v2C3.5 7 1 4.5 1 1z" fill="#777"/></svg>+900125550147 (Phone)</li>
      <li><svg width="8" height="8" viewBox="0 0 8 8"><rect x="1" y="3" width="6" height="3.5" fill="#777"/><rect x="2" y="1" width="4" height="2" fill="#999"/></svg>+900125550147(Fax)</li>
      <li><svg width="8" height="8" viewBox="0 0 8 8"><rect x="0.5" y="1.5" width="7" height="5" fill="#777"/><polyline points="0.5,1.5 4,4.5 7.5,1.5" fill="none" stroke="#fff" stroke-width=".8"/></svg><span class="mail">info@torvelpower.com</span></li>
      <li style="line-height:9px"><svg width="8" height="8" viewBox="0 0 8 8" style="top:0"><path d="M4 0.5a2.6 2.6 0 0 1 2.6 2.6C6.6 5 4 7.5 4 7.5S1.4 5 1.4 3.1A2.6 2.6 0 0 1 4 .5z" fill="#777"/><circle cx="4" cy="3.1" r="1" fill="#f4f5f7"/></svg>Harbor Road&nbsp; Coastal District 40210<br>Republic of Westmarch</li>
    </ul>
  </div>
  <div class="foot-col" style="left:354px">
    <h5>NEWSLETTER</h5>
    <p>Register Your email address to get<br>information about us</p>
    <div class="email-field">Email Address</div>
    <div class="subscribe">SUBSCRIBE</div>
  </div>
  <div class="foot-col" style="left:514px">
    <h5>FOLLOW US</h5>
    <p>Lorem ipsum dolor sit amet, conse<br>ctetur adipiscing elit. Nulla in purus<br>nibh. Donec ornare</p>
    <div class="social"><span></span><span></span><span></span><span></span><span></span></div>
  </div>
</footer>

<div class="copyright">© Copyright 2017 TORVEL POWER .All Rights Reserved</div>

</body>
</html>
```